Verpackungsdesign für Glasprodukte
Super Designvorschläge und in kürzester Zeit ausgearbeitet. Danke für die Unterstützung!
Zielgruppe
Wir sind eine Glaser Handwerksunternehmen die Dienstleistung und Glasprodukte verkaufen, unsere Zielgruppe sind BtoB und BtoC Kunden an die wir hochwertige Produkte für faire Preise anbieten.
Aufgabenstellung
Schlichtes und modernes Design, auf der Vorderseite soll das Logo, innen kommt eine Persönlicher Text und ein Bild von mir

```html
<!DOCTYPE html>
<html lang="de">
<head>
<meta charset="utf-8">
<title>Glaserei Lindholm – Präsentationsmappe</title>
<link href="https://fonts.googleapis.com/css2?family=Mulish:wght@300;400;600&display=swap" rel="stylesheet">
<style>
:root{
  --bg-light:#e4e4e4;
  --bg-dark:#bdbdbd;
  --paper:#f2f2f2;
  --paper-shade:#e6e6e6;
  --band:#716c65;
  --band-dark:#655f59;
  --ink:#2b2b2b;
  --ink-soft:#6f6f6f;
  --on-band:#ecebe8;
  --glass-light:#e9e9e9;
  --glass-mid:#a9a9a9;
  --glass-dark:#5a5a5a;
}
*{box-sizing:border-box;margin:0;padding:0}
html,body{width:1200px;height:1200px;overflow:hidden}
body{
  font-family:"Mulish",sans-serif;
  background:radial-gradient(ellipse at 50% 45%,var(--bg-light) 0%,var(--bg-dark) 100%);
  position:relative;color:var(--ink);
}
.spread{position:absolute;left:120px;width:960px;display:flex;box-shadow:0 12px 30px rgba(0,0,0,.18)}
.spread--inside{top:50px;height:520px}
.spread--outside{top:630px;height:470px;clip-path:polygon(0 0,100% 0,100% 88%,96% 100%,4% 100%,0 88%)}
.panel{position:relative;flex:1;background:linear-gradient(90deg,var(--paper) 0%,var(--paper-shade) 100%);overflow:hidden}
.panel+.panel{border-left:1px solid #d4d4d4}
.band{position:absolute;left:0;right:0;bottom:0;height:44px;background:var(--band);color:var(--on-band);
  font-size:11px;font-weight:300;display:flex;align-items:center;justify-content:center;letter-spacing:.2px}

/* left inside panel */
.contact-block{position:absolute;top:205px;left:0;right:0;text-align:center}
.contact-block .web{font-size:15px;font-weight:600;color:#56524d}
.contact-block .handle{margin-top:10px;font-size:12px;color:#56524d}

/* centre inside panel */
.glass-photo{position:absolute;inset:0 0 44px 0;
  background:radial-gradient(ellipse at 45% 55%,var(--glass-mid) 0%,#cfcfcf 55%,var(--glass-light) 100%)}
.brand-mark{position:absolute;top:170px;left:50%;transform:translateX(-50%);width:160px;height:140px;
  border:3px solid #fff;display:flex;align-items:center;justify-content:center;text-align:center}
.brand-mark span{color:#fff;font-size:19px;font-weight:400;letter-spacing:3px;line-height:1.35}
.pocket{position:absolute;left:10px;right:10px;bottom:0;height:86px;background:var(--band-dark);
  border-radius:12px 12px 0 0}
.pocket::before{content:"";position:absolute;left:0;right:0;top:0;height:34px;background:var(--paper);border-radius:12px 12px 0 0}
.biz-card{position:absolute;left:28px;bottom:6px;width:96px;height:76px;background:#ededed;
  box-shadow:0 1px 3px rgba(0,0,0,.25);display:flex;align-items:center;justify-content:center;text-align:center}
.biz-card span{font-size:8px;letter-spacing:1.5px;color:var(--ink);line-height:1.4;border:1px solid #b59f6a;padding:8px 6px}
.pocket .email{position:absolute;right:22px;bottom:14px;color:var(--on-band);font-size:11px;font-weight:300}

/* right inside panel */
.welcome{position:absolute;top:60px;left:20px;width:140px}
.welcome h2{font-size:15px;font-weight:600;line-height:1.3;color:var(--ink)}
.welcome p{margin-top:14px;font-size:7.6px;font-weight:300;line-height:1.55;color:var(--ink-soft)}
.signature{margin-top:18px;width:70px;height:32px;background:linear-gradient(90deg,#dcdcdc,#e8e8e8)}
.signer{margin-top:12px;font-size:8.5px;font-weight:600;color:var(--ink)}
.signer-role{font-size:8px;font-weight:300;color:var(--ink-soft);margin-top:2px}
.portrait{position:absolute;top:0;right:0;width:150px;bottom:44px;
  background:linear-gradient(180deg,#d9d6d2 0%,#b9aa9c 35%,#3b3b3d 60%,#2f2f31 100%)}

/* outside */
.outside-photo{position:absolute;inset:0 0 62px 0;
  background:linear-gradient(90deg,#e4e4e4 0%,#bdbdbd 40%,#8a8a8a 70%,#d6d6d6 100%)}
.outside-band{position:absolute;left:0;right:0;bottom:0;height:62px;background:var(--band)}
.cover-mark{position:absolute;top:140px;right:44px;width:120px;height:150px;background:#f1f1f1;
  border:2px solid #b59f6a;display:flex;align-items:center;justify-content:center;text-align:center}
.cover-mark span{font-size:14px;letter-spacing:2px;color:var(--ink);line-height:1.4}
</style>
</head>
<body>

<section class="spread spread--inside" aria-label="Innenseite der Mappe">
  <div class="panel panel--contact">
    <div class="contact-block">
      <p class="web">www.glaserei-lindholm.de</p>
      <p class="handle">@glaserei.lindholm</p>
    </div>
    <div class="band">www.glasereilindholm.de</div>
  </div>

  <div class="panel panel--centre">
    <div class="glass-photo" role="img" aria-label="Foto gestaffelter Glasscheiben in Grautönen"></div>
    <div class="brand-mark"><span>GLASEREI<br>LINDHOLM</span></div>
    <div class="pocket">
      <div class="biz-card"><span>GLASEREI<br>LINDHOLM</span></div>
      <p class="email">info@glasereilindholm.de</p>
    </div>
  </div>

  <div class="panel panel--welcome">
    <div class="portrait" role="img" aria-label="Porträtfoto des Geschäftsführers mit verschränkten Armen"></div>
    <div class="welcome">
      <h2>Herzlich Willkommen bei der Glaserei Lindholm</h2>
      <p>Lorem ipsum dolor sit amet, cons ectetuer adipiscing elit, sed diam nonummy nibh euismod tincidunt ut laoreet dolore magna aliquam erat volutpat.</p>
      <p>Lorem ipsum dolor sit amet, consectetuer adipiscing elit, sed diam nonummy nibh euismod tincidunt u v laoreet dolore magna aliquam erat volutpat. Ut wisi enim ad minim veniam, quis nostrud exerci tation.</p>
      <p>Mit freundlichen Grüßen</p>
      <div class="signature" role="img" aria-label="Handschriftliche Unterschrift"></div>
      <p class="signer">Jonas Brandt</p>
      <p class="signer-role">Geschäftsführer</p>
    </div>
    <div class="band">Glaserei Lindholm GmbH &nbsp;|&nbsp; Birkenweg 12 &nbsp;|&nbsp; 25421 Pinneberg</div>
  </div>
</section>

<section class="spread spread--outside" aria-label="Außenseite der Mappe">
  <div class="panel">
    <div class="outside-photo" role="img" aria-label="Foto hintereinander stehender Glasscheiben mit dunklen Kanten"></div>
    <div class="cover-mark"><span>GLASEREI<br>LINDHOLM</span></div>
    <div class="outside-band"></div>
  </div>
</section>

</body>
</html>
```